Pet sitting and Dog Walking Postcard distributed to new home owners in our target market

We need a two-sided postcard (or rack card, size can be anything rack card size or smaller) that is going in a folder that will be distributed each month to new homeowners in our target area. I would like the design to be similar to our brochure which will be uploaded here for you to see. It needs much less information than the brochure.
Should include services we offer; and our 4 systems: online registration, complimentary consultation, flexible scheduling, visits with reports and photos. Should also include our contact information (website, email, phone). Photos from the brochure can be used. Tagline from the cover of the brochure can be used. Call to action should be: Register on our website today to receive a free consultation and $20 off your first booking (when requesting a service, mention the promo code: welcome20).

```html
<!DOCTYPE html>
<html lang="en">
<head>
<meta charset="utf-8">
<title>Paws Harbor Pet Care – Rack Card</title>
<link rel="stylesheet" href="https://fonts.googleapis.com/css2?family=Montserrat:wght@500;600;700;800&family=Open+Sans:ital,wght@0,400;0,600;1,400&family=Oswald:wght@600&display=swap">
<style>
  :root{
    --purple:#4e3a5c;
    --purple-deep:#43314f;
    --green:#3f9a35;
    --green-bright:#4cb842;
    --cream:#efeee8;
    --ink:#3a3a3a;
    --white:#ffffff;
    --stage:#3b3b3e;
  }
  *{box-sizing:border-box;margin:0;padding:0}
  html,body{width:1200px;height:857px;overflow:hidden;background:var(--stage)}
  .canvas{position:relative;width:1200px;height:857px}
  .card{position:absolute;top:28px;width:356px;height:800px;overflow:hidden;box-shadow:0 10px 30px rgba(0,0,0,.45)}
  .card--front{left:214px;background:var(--cream)}
  .card--back{left:630px;background:var(--purple);color:var(--white);font-family:"Open Sans",sans-serif}

  /* front */
  .brand{position:absolute;top:70px;left:0;width:100%;display:flex;align-items:center;justify-content:center;gap:10px}
  .brand__dot{width:14px;height:14px;border-radius:50%;background:var(--green)}
  .brand__name{font-family:"Montserrat",sans-serif;font-weight:800;font-size:24px;line-height:1.05;color:var(--purple);text-align:center;letter-spacing:.5px}
  .hero{position:absolute;top:178px;left:28px;width:300px;height:300px}
  .hero__photo{position:absolute;left:18px;top:18px;width:264px;height:264px;border-radius:50%;border:7px solid var(--purple);
    background:radial-gradient(circle at 45% 40%,#e9e3da 0%,#cdb8a2 40%,#5c4a44 70%,#7f8fa3 100%)}
  .hero svg{position:absolute;inset:0}
  .tagline{position:absolute;top:508px;left:0;width:100%;text-align:center;font-family:"Montserrat",sans-serif;font-weight:800;font-size:21px;line-height:1.25}
  .tagline__lead{color:var(--purple)}
  .tagline__promise{color:var(--green)}
  .offer{position:absolute;top:580px;left:22px;width:312px;height:112px;border:1.5px dashed #666;border-radius:6px;text-align:center;padding-top:10px}
  .offer__line{font-family:"Montserrat",sans-serif;font-weight:800;font-size:12.5px;color:var(--purple);text-transform:none;line-height:1.3}
  .offer__line--caps{text-transform:uppercase;font-size:11.5px}
  .offer__deal{font-family:"Oswald",sans-serif;font-weight:600;font-size:25px;color:var(--green);line-height:1.2;text-transform:uppercase}
  .offer__note{font-size:9.5px;color:var(--ink);font-family:"Open Sans",sans-serif}
  .offer__note b{font-weight:600}
  .band{position:absolute;left:0;bottom:0;width:100%;height:90px;background:var(--purple);display:flex;align-items:center;justify-content:center}
  .band__url{font-family:"Montserrat",sans-serif;font-weight:600;font-size:15px;color:var(--white);letter-spacing:2.4px}

  /* back */
  .services{position:absolute;top:34px;left:24px;right:20px}
  .h-title{font-family:"Montserrat",sans-serif;font-weight:800;font-size:19px;color:var(--white)}
  .h-title em{font-style:normal;color:var(--green-bright)}
  .services__list{display:grid;grid-template-columns:1fr 1.5fr;gap:3px 10px;margin-top:8px;list-style:none;font-family:"Montserrat",sans-serif;font-weight:500;font-size:10.5px}
  .services__list li{display:flex;align-items:center;gap:6px}
  .tick{width:11px;height:11px;flex:none}
  .intro{position:absolute;top:150px;left:24px;right:20px}
  .intro p{font-size:10px;line-height:1.4;margin-top:6px;color:#f1ecf3}
  .systems{position:absolute;top:232px;left:20px;right:18px;list-style:none}
  .system{display:flex;gap:12px;align-items:center;margin-bottom:14px}
  .system__icon{width:46px;height:46px;flex:none;border-radius:50%;background:var(--white);display:flex;align-items:center;justify-content:center}
  .system__title{font-family:"Montserrat",sans-serif;font-weight:700;font-size:13px;color:var(--green-bright)}
  .system__text{font-size:9.8px;line-height:1.38;color:#f1ecf3}
  .credentials{position:absolute;top:556px;left:20px;width:300px;border:1px solid rgba(255,255,255,.45);border-radius:8px;padding:10px 12px;font-family:"Montserrat",sans-serif;font-weight:500;font-size:12.5px;line-height:1.35;color:var(--white)}
  .pet-photo{position:absolute;right:8px;top:630px;width:100px;height:130px;border-radius:40% 40% 20% 20%;background:radial-gradient(circle at 50% 35%,#f6efe2,#e3d3b8 60%,rgba(78,58,92,0) 72%)}
  .contact{position:absolute;top:676px;left:24px}
  .contact__title{font-family:"Montserrat",sans-serif;font-weight:700;font-size:15px;color:var(--green-bright);letter-spacing:.5px;margin-bottom:8px}
  .contact__list{list-style:none;font-size:11px}
  .contact__list li{display:flex;align-items:center;gap:9px;margin-bottom:6px}
  .contact__icon{width:20px;height:20px;border-radius:50%;background:var(--green-bright);display:flex;align-items:center;justify-content:center}
</style>
</head>
<body>
<main class="canvas">

  <!-- Front -->
  <section class="card card--front">
    <div class="brand">
      <span class="brand__dot"></span>
      <span class="brand__name">PAWS HARBOR<br>PET CARE</span>
    </div>

    <div class="hero">
      <div class="hero__photo" role="img" aria-label="Photo of a smiling woman on a sofa cuddling a brown and white spaniel"></div>
      <svg viewBox="0 0 300 300" aria-hidden="true">
        <path d="M52 62 A140 140 0 0 1 262 72" fill="none" stroke="var(--green)" stroke-width="3"/>
        <path d="M18 118 A140 140 0 0 0 70 262" fill="none" stroke="var(--green)" stroke-width="3"/>
        <path d="M276 130 A140 140 0 0 1 150 290" fill="none" stroke="var(--green)" stroke-width="3"/>
      </svg>
    </div>

    <h1 class="tagline">
      <span class="tagline__lead">Prioritize Yourself.</span><br>
      <span class="tagline__promise">We'll Focus on Your Pets.</span>
    </h1>

    <div class="offer">
      <p class="offer__line">Register on our website today</p>
      <p class="offer__line offer__line--caps">To receive a free consultation and</p>
      <p class="offer__deal">$20 off your first booking</p>
      <p class="offer__note">(when requesting a service, mention the promo code: <b>welcome20</b>)</p>
    </div>

    <div class="band"><span class="band__url">www.pawsharborpets.com</span></div>
  </section>

  <!-- Back -->
  <section class="card card--back">
    <div class="services">
      <h2 class="h-title">Professional <em>Pet Care Services</em></h2>
      <ul class="services__list">
        <li><svg class="tick" viewBox="0 0 12 12"><rect x=".75" y=".75" width="10.5" height="10.5" rx="2" fill="none" stroke="#4cb842" stroke-width="1.3"/><path d="M3 6.2l2 2 4-4.4" fill="none" stroke="#4cb842" stroke-width="1.5"/></svg>Dog Walking</li>
        <li><svg class="tick" viewBox="0 0 12 12"><rect x=".75" y=".75" width="10.5" height="10.5" rx="2" fill="none" stroke="#4cb842" stroke-width="1.3"/><path d="M3 6.2l2 2 4-4.4" fill="none" stroke="#4cb842" stroke-width="1.5"/></svg>Day Care and Overnight Boarding</li>
        <li><svg class="tick" viewBox="0 0 12 12"><rect x=".75" y=".75" width="10.5" height="10.5" rx="2" fill="none" stroke="#4cb842" stroke-width="1.3"/><path d="M3 6.2l2 2 4-4.4" fill="none" stroke="#4cb842" stroke-width="1.5"/></svg>Pet Sitting</li>
        <li><svg class="tick" viewBox="0 0 12 12"><rect x=".75" y=".75" width="10.5" height="10.5" rx="2" fill="none" stroke="#4cb842" stroke-width="1.3"/><path d="M3 6.2l2 2 4-4.4" fill="none" stroke="#4cb842" stroke-width="1.5"/></svg>Cat Sitting</li>
        <li><svg class="tick" viewBox="0 0 12 12"><rect x=".75" y=".75" width="10.5" height="10.5" rx="2" fill="none" stroke="#4cb842" stroke-width="1.3"/><path d="M3 6.2l2 2 4-4.4" fill="none" stroke="#4cb842" stroke-width="1.5"/></svg>Sleepovers</li>
        <li><svg class="tick" viewBox="0 0 12 12"><rect x=".75" y=".75" width="10.5" height="10.5" rx="2" fill="none" stroke="#4cb842" stroke-width="1.3"/><path d="M3 6.2l2 2 4-4.4" fill="none" stroke="#4cb842" stroke-width="1.5"/></svg>Small Pet Sitting</li>
      </ul>
    </div>

    <div class="intro">
      <h2 class="h-title">Ready To Free Up <em>Your Time?</em></h2>
      <p>We are here to uncomplicate your life! Our systems and processes allow for seamless scheduling, service and billing. Give us a few minutes of your time and we will deliver it back to you tenfold!</p>
    </div>

    <ol class="systems">
      <li class="system">
        <span class="system__icon"><svg width="26" height="22" viewBox="0 0 26 22"><rect x="1" y="1" width="24" height="15" rx="2" fill="#4e3a5c"/><rect x="3" y="3" width="20" height="11" fill="#cfe9cb"/><rect x="10" y="17" width="6" height="3" fill="#4e3a5c"/></svg></span>
        <div><h3 class="system__title">Online Registration</h3>
        <p class="system__text">Click on the register link on our homepage to begin online registration or submit a request form if you would like more information first.</p></div>
      </li>
      <li class="system">
        <span class="system__icon"><svg width="26" height="22" viewBox="0 0 26 22"><path d="M3 2h20a2 2 0 0 1 2 2v10a2 2 0 0 1-2 2H10l-5 4v-4H3a2 2 0 0 1-2-2V4a2 2 0 0 1 2-2z" fill="#3f9a35"/><circle cx="8" cy="9" r="1.5" fill="#fff"/><circle cx="13" cy="9" r="1.5" fill="#fff"/><circle cx="18" cy="9" r="1.5" fill="#fff"/></svg></span>
        <div><h3 class="system__title">Complimentary Consultation</h3>
        <p class="system__text">Request a consultation through our online portal. We'll reach out to you if you get stuck! Then we'll coordinate a meeting at your convenience.</p></div>
      </li>
      <li class="system">
        <span class="system__icon"><svg width="24" height="22" viewBox="0 0 24 22"><rect x="1" y="3" width="22" height="18" rx="2" fill="#fff" stroke="#4e3a5c" stroke-width="2"/><rect x="1" y="3" width="22" height="5" fill="#4e3a5c"/><path d="M5 12h3M10 12h3M15 12h3M5 16h3M10 16h3" stroke="#3f9a35" stroke-width="2"/></svg></span>
        <div><h3 class="system__title">Flexible Scheduling</h3>
        <p class="system__text">Once we've met, we will be able to custom schedule your visits to fit your needs. You can always adjust your schedule through our portal app if your needs change.</p></div>
      </li>
      <li class="system">
        <span class="system__icon"><svg width="26" height="20" viewBox="0 0 26 20"><rect x="1" y="4" width="24" height="15" rx="3" fill="#4e3a5c"/><rect x="8" y="1" width="10" height="4" rx="1" fill="#4e3a5c"/><circle cx="13" cy="11.5" r="4.5" fill="#fff"/><circle cx="13" cy="11.5" r="2.5" fill="#3f9a35"/></svg></span>
        <div><h3 class="system__title">Visits with Reports and Photos</h3>
        <p class="system__text">Your pets will be cared for by our elite team of Pet Care Specialists. After each visit, you will receive an emailed report with photo.</p></div>
      </li>
    </ol>

    <p class="credentials">Fully Insured and Bonded Professional Pet Care Specialists Proudly Serving Maple Valley and Surrounding Neighborhoods Since 2004</p>

    <div class="pet-photo" role="img" aria-label="Photo of a sitting yellow Labrador puppy with a blue collar"></div>

    <div class="contact">
      <h2 class="contact__title">CONTACT US</h2>
      <ul class="contact__list">
        <li><span class="contact__icon"><svg width="11" height="11" viewBox="0 0 12 12"><path d="M2.5 1l2 2.5-1.2 1.3a7 7 0 0 0 3.9 3.9l1.3-1.2 2.5 2-1 1.5C5.5 11 1 6.5 1 2.5z" fill="#fff"/></svg></span>555-014-BARK</li>
        <li><span class="contact__icon"><svg width="11" height="9" viewBox="0 0 12 9"><rect x=".5" y=".5" width="11" height="8" fill="#fff"/><path d="M.5 .8L6 5l5.5-4.2" fill="none" stroke="#4cb842"/></svg></span>hello@pawsharborpets.com</li>
        <li><span class="contact__icon"><svg width="12" height="12" viewBox="0 0 12 12"><circle cx="6" cy="6" r="5" fill="none" stroke="#fff"/><ellipse cx="6" cy="6" rx="2.2" ry="5" fill="none" stroke="#fff"/><path d="M1 6h10" stroke="#fff"/></svg></span>www.pawsharborpets.com</li>
      </ul>
    </div>
  </section>

</main>
</body>
</html>
```